Veltrano Energy Business Card Design

website: www.veltranoenergy.example
Project: Business Card Design for Veltrano Energy
Name: Dorian Kettle
Title: Founder / Operations Strategist
Visual Identity & Logo:
Logo File: VEL-Logo-FullGradient-Final.png (Attached).
Color Palette: The brand relies on a distinctive Cyan (Blue) to Lime Green gradient.
Background Preference: We want a Dark Mode aesthetic (Deep Matte Black, Charcoal, or Dark Slate) to make the neon gradient of the logo pop. This feels more "tech/industrial" than a standard white card.
Design Aesthetic (The "Ops" Vibe):
Concept: "Grid & Infrastructure." We are a solar rental company, focusing on logistics and access.
Typography: White, bold sans-serif text for contact info. High contrast against the dark background.
Accents: Use the Cyan or Lime Green from the logo for thin divider lines or edge painting.
Avoid: No orange/gold (clashes with logo). No cartoon leaves.
Layout Requirements:
Front: Large, centered logo. Maybe a subtle UV gloss spot varnish over the logo icon.
Back: Name, Title, Contact Info.
Texture: Matte finish cardstock with gloss elements.
sample mock up of information on card: https://brivomarkco-my.filehost.example/:i:/g/personal/dorian_kettle_veltranoenergy_example/AbCdEfGhIjKlMnOpQrStUvWxYz012345678?e=Xy12Ab
Logo: https://brivomarkco.filehost.example/:i:/s/VeltranoEnergy/ZyXwVuTsRqPoNmLkJiHgFeDcBa9876543210?e=Pq34Cd

```html
<!DOCTYPE html>
<html lang="en">
<head>
<meta charset="utf-8">
<title>Veltrano Energy – Business Card</title>
<link href="https://fonts.googleapis.com/css2?family=Lato:ital,wght@0,400;0,700;0,900;1,900&display=swap" rel="stylesheet">
<style>
  :root {
    --stage: #1e2a2a;
    --card: #2a2a2b;
    --card-deep: #222223;
    --cyan: #2fc6d8;
    --lime: #a6d61e;
    --white: #f4f5f5;
    --muted: #c9cccc;
    --chip: #d9dcdc;
  }
  * { margin: 0; padding: 0; box-sizing: border-box; }
  html, body { width: 1200px; height: 880px; overflow: hidden; }
  body {
    background: var(--stage);
    font-family: "Lato", sans-serif;
    display: flex;
    flex-direction: column;
    align-items: center;
    justify-content: center;
    gap: 44px;
  }
  .card-edge {
    width: 640px;
    height: 366px;
    border-radius: 22px;
    padding: 0 0 4px 3px;
    background: linear-gradient(90deg, var(--cyan), var(--lime));
    box-shadow: 0 18px 40px rgba(0,0,0,.45);
  }
  .card {
    position: relative;
    width: 100%;
    height: 100%;
    border-radius: 20px;
    background: var(--card);
    overflow: hidden;
  }

  /* Front */
  .front-pattern {
    position: absolute; inset: 0;
    background: radial-gradient(ellipse at 75% 30%, #343435 0%, var(--card) 55%, var(--card-deep) 100%);
  }
  .front-brand {
    position: absolute;
    left: 0; right: 0; top: 128px;
    display: flex; align-items: center; justify-content: center; gap: 22px;
  }
  .brand-square {
    width: 58px; height: 58px;
    background: var(--cyan);
    border-radius: 6px;
  }
  .brand-name {
    font-weight: 700;
    font-size: 62px;
    letter-spacing: 1px;
    color: var(--cyan);
  }
  .region-dots {
    position: absolute;
    left: 0; right: 0; top: 238px;
    display: flex; justify-content: center; gap: 10px;
  }
  .region-dot {
    width: 28px; height: 28px; border-radius: 50%;
    background: var(--chip);
  }

  /* Back */
  .back-mark {
    position: absolute;
    right: 26px; top: 26px;
    width: 250px; height: 250px;
    border-radius: 24px;
    background: linear-gradient(150deg, #4a4a4b 0%, #2f2f30 60%, #262627 100%);
  }
  .back-info {
    position: absolute;
    left: 46px; top: 46px;
    width: 310px;
    color: var(--white);
  }
  .person-name {
    font-weight: 900;
    font-size: 34px;
    letter-spacing: .5px;
    line-height: 1;
  }
  .person-title {
    font-size: 17px;
    color: var(--muted);
    margin-top: 6px;
  }
  .divider {
    width: 290px;
    height: 2px;
    background: linear-gradient(90deg, var(--cyan), var(--lime));
    margin: 12px 0 14px;
  }
  .contact-list { list-style: none; font-size: 16px; line-height: 1.35; }
  .contact-item { display: flex; gap: 12px; align-items: flex-start; }
  .contact-icon { width: 16px; height: 16px; flex: none; margin-top: 3px; fill: none; stroke: var(--white); stroke-width: 1.6; }
  .address-item { margin-bottom: 2px; }
  .tagline {
    position: absolute;
    left: 46px; bottom: 30px;
    width: 520px;
    font-style: italic;
    font-weight: 900;
    font-size: 16px;
    color: var(--white);
    white-space: nowrap;
  }
  .tagline-rule {
    position: absolute;
    left: 46px; bottom: 62px;
    width: 300px; height: 2px;
    background: linear-gradient(90deg, var(--cyan), var(--lime));
  }
</style>
</head>
<body>

<section class="card-edge card-front" aria-label="Card front">
  <div class="card">
    <div class="front-pattern" role="img" aria-label="Faint gloss pattern of the brand symbol repeated across the card"></div>
    <div class="front-brand">
      <span class="brand-square"></span>
      <span class="brand-name">Veltrano Energy</span>
    </div>
    <div class="region-dots" aria-label="Service regions">
      <span class="region-dot"></span>
      <span class="region-dot"></span>
      <span class="region-dot"></span>
    </div>
  </div>
</section>

<section class="card-edge card-back" aria-label="Card back">
  <div class="card">
    <div class="back-mark" role="img" aria-label="Large gloss spot varnish brand symbol"></div>
    <div class="back-info">
      <h1 class="person-name">DORIAN KETTLE</h1>
      <p class="person-title">Founder / Operations Strategist</p>
      <div class="divider"></div>
      <ul class="contact-list">
        <li class="contact-item address-item">
          <svg class="contact-icon" viewBox="0 0 16 16"><path d="M8 15s5-5 5-9a5 5 0 0 0-10 0c0 4 5 9 5 9z"/><circle cx="8" cy="6" r="1.8"/></svg>
          <span>Veltrano Energy<br>4210 Harrow Point Drive<br>Fernmoor, FL 30000</span>
        </li>
        <li class="contact-item">
          <svg class="contact-icon" viewBox="0 0 16 16"><path d="M3 2h3l1.5 3.5-2 1.2a8 8 0 0 0 3.8 3.8l1.2-2L14 10v3a1 1 0 0 1-1 1A12 12 0 0 1 2 3a1 1 0 0 1 1-1z"/></svg>
          <span>555.014.2290</span>
        </li>
        <li class="contact-item">
          <svg class="contact-icon" viewBox="0 0 16 16"><rect x="1.5" y="3.5" width="13" height="9" rx="1"/><path d="M1.5 4l6.5 5 6.5-5"/></svg>
          <span>info@veltranoenergy.example</span>
        </li>
        <li class="contact-item">
          <svg class="contact-icon" viewBox="0 0 16 16"><circle cx="8" cy="8" r="6.5"/><path d="M1.5 8h13M8 1.5c2 2 2 11 0 13M8 1.5c-2 2-2 11 0 13"/></svg>
          <span>www.veltranoenergy.example</span>
        </li>
      </ul>
    </div>
    <div class="tagline-rule"></div>
    <p class="tagline">Clear Terms, Steady Power, Simple Access, Real Value.</p>
  </div>
</section>

</body>
</html>
```